National Virtual CPA Firm needs post card design

Virtual CPA firm called "QUINDRA" needs a 5.5” x 8.5” post card designed to market our services to middle market mid-size american businesses. We provide Full Service Payroll (includes the processing of payroll, printing of checks and direct depositing, tax filing, and tax payments), Bookkeeping (Using their native systems, or ours), Contract CFO (with expense reduction analysis), Reporting services for business directors to make informed decisions, Capital Fundraising (Advice on seeking equity to help grow your business), and Taxes (Personal (1040), Partnership (1065), Corporate (1120, 1120S (Including Consolidated Returns)), Trust (1041) and Non-Profit (990)), including all affiliated state returns. One of our major selling points is our variety of experience, and our fast turn around times on projects.
This project specifically, I would like to highlight the bookkeeping services, but still want the tax and payroll services listed on the postcard.
I have uploaded the logo design for QUINDRA and would like a postcard that compliments the logo.
Company contact info is:
Quindra accounting services Inc
P.O. Box 4586
Cedar Bend, ID 83471
(800) 362-9174
Www.quindra-example.com
Target Market(s)
Small to medium size businesses
Industry/Entity Type
Accounting

```html
<!DOCTYPE html>
<html lang="en">
<head>
<meta charset="utf-8">
<title>Quindra Postcard</title>
<link href="https://fonts.googleapis.com/css2?family=Poppins:wght@400;500;600;700&display=swap" rel="stylesheet">
<style>
:root{
  --green:#4cb848;
  --green-dark:#2f8f3a;
  --lime:#8cc63f;
  --yellow:#fcc12e;
  --ink:#141414;
  --white:#ffffff;
  --paper-grey:#d9dbda;
  --backdrop:#b9b8b4;
  --photo-a:#c9d3dc;
  --photo-b:#7f8fa3;
}
*{margin:0;padding:0;box-sizing:border-box}
html,body{width:696px;height:1200px;overflow:hidden}
body{background:var(--backdrop);font-family:'Poppins',sans-serif;color:var(--ink);position:relative}
.card{position:absolute;left:28px;width:640px;height:414px;overflow:hidden;background:var(--white);box-shadow:0 6px 18px rgba(0,0,0,.18)}
.card--front{top:168px}
.card--back{top:618px}
.card-shapes{position:absolute;inset:0;width:640px;height:414px}
.abs{position:absolute}
.brand{display:flex;align-items:center;gap:7px;font-weight:700;letter-spacing:.5px;color:var(--ink)}
.brand-dot{width:14px;height:14px;border-radius:50%;background:var(--yellow)}
.brand--front{left:20px;top:28px;font-size:24px}
.brand--back{left:380px;top:26px;font-size:20px}
.brand--back .brand-dot{width:12px;height:12px}
.headline{left:19px;top:88px;font-size:27px;line-height:31px;font-weight:600;white-space:nowrap}
.headline .hl{color:var(--green)}
.pill{background:var(--green);color:var(--white);font-weight:600;border-radius:10px;font-size:10.5px;height:18px;line-height:18px;padding:0 11px;white-space:nowrap}
.pill--light{background:var(--white);color:var(--ink)}
.usp-row{left:20px;top:267px;display:flex;align-items:center;font-size:9.5px;line-height:11px;font-weight:500}
.usp{display:flex;align-items:center;gap:6px}
.icon-disc{width:22px;height:22px;border-radius:50%;background:var(--green);display:flex;align-items:center;justify-content:center;flex:none}
.icon-disc svg{width:13px;height:13px}
.divider{width:1px;height:14px;background:var(--ink);margin:0 16px}
.contact-row{left:20px;top:377px;display:flex;align-items:center;color:var(--white);font-size:10px;font-weight:500;letter-spacing:.4px}
.contact-row .divider{background:var(--white);margin:0 11px}
.contact-item{display:flex;align-items:center;gap:6px;white-space:nowrap}
.contact-item .icon-disc{width:17px;height:17px}
.contact-item .icon-disc svg{width:10px;height:10px}
.services{left:20px;top:52px;width:300px;color:var(--white)}
.service{display:flex;align-items:flex-start;gap:8px;height:33px}
.service .icon-disc{background:var(--white);width:20px;height:20px;margin-top:2px;position:relative}
.service .icon-disc::after{content:"";position:absolute;right:-6px;top:6px;border:4px solid transparent;border-left:4px solid var(--yellow)}
.service-title{font-size:10px;font-weight:600;line-height:12px}
.service-desc{font-size:7px;line-height:9px;opacity:.95}
.extras{left:20px;top:264px;color:var(--white);display:grid;grid-template-columns:98px 80px 130px;row-gap:7px}
.extra{display:flex;gap:5px;align-items:flex-start}
.tick{width:10px;height:10px;border-radius:50%;background:var(--white);flex:none;margin-top:2px;display:flex;align-items:center;justify-content:center}
.tick svg{width:7px;height:7px}
.extra-title{font-size:9.5px;font-weight:600;line-height:10px}
.extra-desc{font-size:7px;line-height:8.5px}
.stamp{left:546px;top:19px;width:75px;height:75px;background:var(--paper-grey);display:flex;align-items:center;justify-content:center;text-align:center;font-size:9.5px;line-height:14px;font-weight:500}
.address-line{height:1px;background:var(--ink);left:333px;width:289px}
</style>
</head>
<body>

<section class="card card--front" aria-label="Postcard front">
  <svg class="card-shapes" viewBox="0 0 640 414" aria-hidden="true">
    <defs>
      <linearGradient id="photoTone" x1="0" y1="0" x2="1" y2="1">
        <stop offset="0" stop-color="#9aa6b4"/>
        <stop offset=".5" stop-color="var(--photo-a)"/>
        <stop offset="1" stop-color="var(--photo-b)"/>
      </linearGradient>
      <linearGradient id="photoFade" x1="0" y1="0" x2="1" y2="0">
        <stop offset="0" stop-color="#fff" stop-opacity="1"/>
        <stop offset="1" stop-color="#fff" stop-opacity="0"/>
      </linearGradient>
    </defs>
    <rect x="0" y="0" width="640" height="414" fill="#fff"/>
  </svg>
  <svg class="card-shapes" viewBox="0 0 640 414" role="img" aria-label="Photo of a person at a desk reviewing bar and pie chart reports beside a calculator">
    <path d="M262 0 H640 V414 H262 Z" fill="url(#photoTone)"/>
    <rect x="262" y="0" width="110" height="414" fill="url(#photoFade)"/>
  </svg>
  <svg class="card-shapes" viewBox="0 0 640 414" aria-hidden="true">
    <path d="M188 0 H222 C270 34 302 82 318 132 C292 88 250 38 188 0 Z" fill="var(--green)"/>
    <path d="M0 292 C150 266 330 294 520 364 L0 414 Z" fill="var(--yellow)"/>
    <path d="M0 316 C160 290 330 320 500 364 C580 382 625 352 640 316 V414 H0 Z" fill="var(--ink)"/>
    <path d="M560 372 C600 364 628 340 640 300 V316 C626 350 600 370 560 372 Z" fill="var(--lime)"/>
  </svg>

  <div class="abs brand brand--front"><span>QUINDRA</span><span class="brand-dot"></span></div>

  <h1 class="abs headline">Best help in<br>your <span class="hl">Bookkeeping,</span><br><span class="hl">Tax</span> and <span class="hl">Payroll</span><br>requirements.</h1>

  <div class="abs pill" style="left:20px;top:236px">We Are Experts</div>

  <div class="abs usp-row">
    <div class="usp">
      <span class="icon-disc"><svg viewBox="0 0 16 16" fill="none" stroke="#fff" stroke-width="1.4"><circle cx="8" cy="5" r="2"/><circle cx="3.5" cy="7" r="1.5"/><circle cx="12.5" cy="7" r="1.5"/><path d="M4.5 14c0-2.5 1.5-4 3.5-4s3.5 1.5 3.5 4"/></svg></span>
      <span>Variety<br>Of Experience</span>
    </div>
    <span class="divider"></span>
    <div class="usp">
      <span class="icon-disc"><svg viewBox="0 0 16 16" fill="none" stroke="#fff" stroke-width="1.4"><circle cx="8.5" cy="8" r="5.5"/><path d="M8.5 5v3.2l2.2 1.4M1 6h3M1.5 9h2.5"/></svg></span>
      <span>Fast Turn Around<br>Times On Projects</span>
    </div>
  </div>

  <div class="abs pill" style="left:20px;top:348px">Contact Us</div>

  <div class="abs contact-row">
    <div class="contact-item"><span class="icon-disc"><svg viewBox="0 0 16 16" fill="none" stroke="#fff" stroke-width="1.6"><path d="M3 2h3l1 3.5-2 1.2a8 8 0 0 0 4.3 4.3l1.2-2L14 10v3a1 1 0 0 1-1 1A11 11 0 0 1 2 3a1 1 0 0 1 1-1z"/></svg></span>(800) 362-9174</div>
    <span class="divider"></span>
    <div class="contact-item"><span class="icon-disc"><svg viewBox="0 0 16 16" fill="none" stroke="#fff" stroke-width="1.4"><circle cx="8" cy="8" r="6"/><path d="M2 8h12M8 2c2 2 2 10 0 12M8 2c-2 2-2 10 0 12"/></svg></span>www.quindra-example.com</div>
    <span class="divider"></span>
    <div class="contact-item"><span class="icon-disc"><svg viewBox="0 0 16 16" fill="none" stroke="#fff" stroke-width="1.6"><path d="M8 15s5-5 5-8.5A5 5 0 0 0 3 6.5C3 10 8 15 8 15z"/><circle cx="8" cy="6.5" r="1.8"/></svg></span>Cedar Bend, ID 83471</div>
  </div>
</section>

<section class="card card--back" aria-label="Postcard back">
  <svg class="card-shapes" viewBox="0 0 640 414" aria-hidden="true">
    <defs>
      <linearGradient id="greenField" x1="0" y1="0" x2="1" y2="1">
        <stop offset="0" stop-color="var(--green-dark)"/>
        <stop offset=".55" stop-color="var(--green)"/>
        <stop offset="1" stop-color="#3fa645"/>
      </linearGradient>
    </defs>
    <rect width="640" height="414" fill="url(#greenField)"/>
    <path d="M0 330 C80 314 150 318 220 340 C150 328 80 328 0 344 Z" fill="var(--yellow)"/>
    <path d="M0 338 C100 320 210 334 290 370 C330 388 365 404 405 414 H0 Z" fill="var(--ink)"/>
    <path d="M322 352 C350 382 380 404 412 414 H400 C372 404 344 384 322 352 Z" fill="var(--yellow)"/>
    <path d="M358 0 H386 C350 42 322 96 312 152 C298 232 322 300 362 360 C314 302 286 232 298 152 C308 92 330 40 358 0 Z" fill="var(--lime)"/>
    <path d="M382 0 H640 V414 H412 C340 352 300 262 308 168 C314 100 344 40 382 0 Z" fill="#fff"/>
  </svg>

  <div class="abs pill pill--light" style="left:20px;top:19px">We Provide Full Service</div>

  <div class="abs services">
    <div class="service">
      <span class="icon-disc"><svg viewBox="0 0 16 16" fill="none" stroke="#333" stroke-width="1.4"><rect x="2" y="4" width="12" height="8" rx="1"/><circle cx="8" cy="8" r="2"/></svg></span>
      <div><div class="service-title">Payroll</div><div class="service-desc">(includes the processing of payroll, printing of checks<br>and direct depositing, tax filing and tax payments).</div></div>
    </div>
    <div class="service" style="margin-top:8px">
      <span class="icon-disc"><svg viewBox="0 0 16 16" fill="none" stroke="#333" stroke-width="1.4"><path d="M3 3h7v10H3zM10 5h3v8h-3"/></svg></span>
      <div><div class="service-title">Bookkeeping</div><div class="service-desc">(Using their native systems, or ours).</div></div>
    </div>
    <div class="service">
      <span class="icon-disc"><svg viewBox="0 0 16 16" fill="none" stroke="#333" stroke-width="1.4"><circle cx="7" cy="7" r="4.5"/><path d="M10.5 10.5L14 14M5 7.5l1.5 1.5 3-3"/></svg></span>
      <div><div class="service-title">Contract CFO</div><div class="service-desc">(with expense reduction analysis).</div></div>
    </div>
    <div class="service">
      <span class="icon-disc"><svg viewBox="0 0 16 16" fill="none" stroke="#333" stroke-width="1.4"><rect x="3" y="2" width="10" height="12"/><path d="M5.5 12V9M8 12V6M10.5 12V8"/></svg></span>
      <div><div class="service-title">Reporting services</div><div class="service-desc">(for business directors to make informed decisions).</div></div>
    </div>
    <div class="service">
      <span class="icon-disc"><svg viewBox="0 0 16 16" fill="none" stroke="#333" stroke-width="1.4"><circle cx="8" cy="6" r="3"/><path d="M2 12c2 0 3 2 6 2s4-2 6-2"/></svg></span>
      <div><div class="service-title">Capital Fundraising</div><div class="service-desc">(Advice on seeking equity to help grow your business).</div></div>
    </div>
  </div>

  <div class="abs pill pill--light" style="left:20px;top:234px">Our Additional Services</div>

  <div class="abs extras">
    <div class="extra"><span class="tick"><svg viewBox="0 0 8 8" fill="none" stroke="#2f8f3a" stroke-width="1.4"><path d="M1.5 4l1.8 1.8L6.5 2.5"/></svg></span><div><div class="extra-title">Taxes</div><div class="extra-desc">(Personal (1040)</div></div></div>
    <div class="extra"><span class="tick"><svg viewBox="0 0 8 8" fill="none" stroke="#2f8f3a" stroke-width="1.4"><path d="M1.5 4l1.8 1.8L6.5 2.5"/></svg></span><div><div class="extra-title">Trust</div><div class="extra-desc">(1041)</div></div></div>
    <div class="extra" style="grid-row:span 2"><span class="tick"><svg viewBox="0 0 8 8" fill="none" stroke="#2f8f3a" stroke-width="1.4"><path d="M1.5 4l1.8 1.8L6.5 2.5"/></svg></span><div><div class="extra-title">Corporate</div><div class="extra-desc">(1120, 1120S) Including<br>Consolidated Returns)</div></div></div>
    <div class="extra"><span class="tick"><svg viewBox="0 0 8 8" fill="none" stroke="#2f8f3a" stroke-width="1.4"><path d="M1.5 4l1.8 1.8L6.5 2.5"/></svg></span><div><div class="extra-title">Partnership</div><div class="extra-desc">(1065)</div></div></div>
    <div class="extra"><span class="tick"><svg viewBox="0 0 8 8" fill="none" stroke="#2f8f3a" stroke-width="1.4"><path d="M1.5 4l1.8 1.8L6.5 2.5"/></svg></span><div><div class="extra-title">Non-Profit</div><div class="extra-desc">(990)</div></div></div>
  </div>

  <div class="abs pill" style="left:20px;top:348px">Contact Us</div>

  <div class="abs contact-row">
    <div class="contact-item"><span class="icon-disc"><svg viewBox="0 0 16 16" fill="none" stroke="#fff" stroke-width="1.6"><path d="M3 2h3l1 3.5-2 1.2a8 8 0 0 0 4.3 4.3l1.2-2L14 10v3a1 1 0 0 1-1 1A11 11 0 0 1 2 3a1 1 0 0 1 1-1z"/></svg></span>(800) 362-9174</div>
    <span class="divider"></span>
    <div class="contact-item"><span class="icon-disc"><svg viewBox="0 0 16 16" fill="none" stroke="#fff" stroke-width="1.4"><circle cx="8" cy="8" r="6"/><path d="M2 8h12M8 2c2 2 2 10 0 12M8 2c-2 2-2 10 0 12"/></svg></span>www.quindra-example.com</div>
  </div>

  <div class="abs brand brand--back"><span>QUINDRA</span><span class="brand-dot"></span></div>
  <div class="abs pill" style="left:378px;top:77px;display:flex;align-items:center;gap:5px;font-size:10px">
    <svg width="9" height="9" viewBox="0 0 16 16" fill="none" stroke="#fff" stroke-width="1.8"><path d="M8 15s5-5 5-8.5A5 5 0 0 0 3 6.5C3 10 8 15 8 15z"/><circle cx="8" cy="6.5" r="1.8"/></svg>
    Cedar Bend, ID 83471
  </div>

  <div class="abs stamp">P.O.<br>Box 4586</div>

  <div class="abs address-line" style="top:156px"></div>
  <div class="abs address-line" style="top:206px;left:330px;width:292px"></div>
  <div class="abs address-line" style="top:257px"></div>
</section>

</body>
</html>
```